New book cover for existing E-Bike tour book

I would like to update the current design of my book "Pedal Trails of the Brackenmoor" (translation: Pedal Trails of the Brackenmoor) and make it more modern.

Existing Book:
Title: "Pedal trails of the Brackenmoor"
Subtitle: 40 eventful tours with nature and culture.
Info bar with three elements:
 Unique sights
 Cozy beer gardens
 The most beautiful bike paths

objectives:
- to make the design more modern
- to make it attractive for people who want to ride E-bike

Requirements for the new design:

1. All texts for title, subtitle and info bar should be kept.
Font, color and placement can be changed.

2. the 5 nature images below the title are optional: can be used, can be replaced, can be omitted

3. the background image is optional: can be used or can be replaced with a totally different background.

Target Market(s)

People who want to discover the "Odenwald" region with the E-Bike

Font styles to use
Sans Serif

Requirements
Must have
• all texts for title, subtitle and info bar should be kept.
Nice to have
• It would be nice to see two E-bike riders. Like on the original book cover but just bigger in size. The two E-Bike riders on the original cover are a bit small.

```html
<!DOCTYPE html>
<html lang="en">
<head>
<meta charset="utf-8">
<title>Pedal Trails of the Brackenmoor — Book Cover</title>
<link rel="stylesheet" href="https://fonts.googleapis.com/css2?family=Bebas+Neue&family=Open+Sans:wght@400;500&display=swap">
<style>
  :root {
    --white: #ffffff;
    --yellow: #ffe100;
    --forest-dark: #1f3315;
    --forest-mid: #3d5a22;
    --forest-light: #6f8f3a;
    --mist: #8b97a0;
    --sky: #b5bcc4;
    --road: #6f7378;
    --road-dark: #4c5055;
    --tag-bg: rgba(95, 100, 104, 0.6);
    --rule: rgba(200, 200, 200, 0.75);
  }
  html, body {
    margin: 0;
    padding: 0;
    width: 800px;
    height: 1200px;
    overflow: hidden;
    background: #222;
  }
  .cover {
    position: relative;
    width: 800px;
    height: 1200px;
    overflow: hidden;
    font-family: "Open Sans", Arial, sans-serif;
    color: var(--white);
  }
  .cover-photo {
    position: absolute;
    inset: 0;
    background:
      linear-gradient(180deg, transparent 0%, transparent 62%, rgba(111,115,120,0.0) 64%, var(--road) 78%, var(--road-dark) 100%),
      linear-gradient(90deg, var(--forest-mid) 0%, var(--forest-light) 18%, var(--forest-dark) 38%, rgba(60,78,60,0.9) 50%, var(--forest-mid) 62%, var(--forest-light) 80%, var(--forest-dark) 100%),
      var(--forest-mid);
  }
  .cover-photo::before {
    content: "";
    position: absolute;
    left: 22%;
    right: 22%;
    top: 0;
    height: 55%;
    background: radial-gradient(ellipse at 50% 20%, var(--sky) 0%, var(--mist) 35%, transparent 75%);
    opacity: 0.85;
  }
  .subtitle {
    position: absolute;
    top: 72px;
    left: 0;
    width: 100%;
    text-align: center;
    font-size: 29px;
    font-weight: 400;
    line-height: 31px;
    letter-spacing: 0.2px;
    text-transform: uppercase;
    margin: 0;
  }
  .title {
    position: absolute;
    top: 170px;
    left: 0;
    width: 100%;
    margin: 0;
    text-align: center;
    font-family: "Bebas Neue", Impact, sans-serif;
    font-weight: 400;
  }
  .title-main {
    display: block;
    font-size: 140px;
    line-height: 140px;
    letter-spacing: 5px;
  }
  .title-connector {
    display: flex;
    align-items: center;
    justify-content: center;
    gap: 14px;
    margin-top: -4px;
    font-size: 94px;
    line-height: 94px;
    letter-spacing: 3px;
  }
  .title-connector .rule {
    width: 150px;
    height: 10px;
    background: linear-gradient(90deg, transparent, var(--rule) 40%, var(--rule));
  }
  .title-connector .rule.right {
    background: linear-gradient(90deg, var(--rule), var(--rule) 60%, transparent);
  }
  .title-place {
    display: block;
    margin-top: 8px;
    font-size: 136px;
    line-height: 136px;
    letter-spacing: 4px;
    color: var(--yellow);
  }
  .info-bar {
    position: absolute;
    top: 960px;
    left: 0;
    width: 100%;
    margin: 0;
    padding: 0;
    list-style: none;
    display: flex;
    flex-direction: column;
    align-items: center;
  }
  .info-bar li {
    background: var(--tag-bg);
    font-size: 35px;
    line-height: 38px;
    padding: 0 6px;
  }
  .author {
    position: absolute;
    top: 1108px;
    left: 0;
    width: 100%;
    margin: 0;
    text-align: center;
    font-family: "Bebas Neue", Impact, sans-serif;
    font-weight: 400;
    font-size: 72px;
    line-height: 72px;
    letter-spacing: 1px;
  }
</style>
</head>
<body>
  <main class="cover">
    <div class="cover-photo" role="img" aria-label="Two cyclists in bright orange and yellow jackets riding along a quiet road through a misty conifer forest"></div>

    <p class="subtitle">40 eventful tours with nature and culture.<br>Info bar with three elements</p>

    <h1 class="title">
      <span class="title-main">Pedal Trails</span>
      <span class="title-connector"><span class="rule"></span>of the<span class="rule right"></span></span>
      <span class="title-place">Brackenmoor</span>
    </h1>

    <ul class="info-bar">
      <li>Unique sights</li>
      <li>Cozy beer gardens</li>
      <li>The most beautiful bike paths</li>
    </ul>

    <p class="author">Anselm Kettering</p>
  </main>
</body>
</html>
```